Easter & Summer School Dance Camps

I need two flyers one for Easter camps and one for summer school
We are a performing arts and dance academy

I want a double sided flyers one side summer school one side easter camp

Please make these flyers appeal to young dancers and performers - eye catching up to date Added Tuesday, March 1, 2016

Target Market(s)

Young children and teenagers

Industry/Entity Type

School

Font styles to use
Serif
Sans Serif

Requirements
Must have
• bright colourful

```html
<!DOCTYPE html>
<html lang="en">
<head>
<meta charset="utf-8">
<title>Once Upon a Time – Easter Workshops</title>
<link rel="stylesheet" href="https://fonts.googleapis.com/css2?family=Montserrat:wght@900&family=Yellowtail&family=Oswald:wght@400;600&family=Roboto+Condensed:wght@400;700&family=Roboto:wght@300&family=Arimo:wght@400;700&family=Archivo+Black&display=swap">
<style>
  :root {
    --magenta: #e62bd8;
    --violet: #a04ae0;
    --sky: #2a9be0;
    --sea: #1f6fd8;
    --deep: #1230b8;
    --navy: #0e2a8a;
    --white: #ffffff;
    --yellow: #f7f21a;
    --band: rgba(255, 255, 255, 0.18);
  }
  * { margin: 0; padding: 0; box-sizing: border-box; }
  html, body { width: 927px; height: 1200px; overflow: hidden; background: var(--navy); }
  .flyer {
    position: relative;
    width: 927px;
    height: 1200px;
    overflow: hidden;
    color: var(--white);
    font-family: "Arimo", sans-serif;
  }
  .scene {
    position: absolute;
    inset: 0;
    background: linear-gradient(180deg, var(--magenta) 0%, var(--violet) 18%, var(--sky) 32%, var(--sea) 55%, var(--deep) 78%, var(--navy) 100%);
  }
  .academy {
    position: absolute;
    top: 78px;
    left: 0;
    width: 100%;
    text-align: center;
    font-family: "Arimo", sans-serif;
    font-weight: 400;
  }
  .academy-name { font-size: 54px; line-height: 1; letter-spacing: 1px; }
  .academy-sub { font-size: 9px; letter-spacing: 0.5px; text-transform: uppercase; margin-top: 20px; }
  .band {
    position: absolute;
    left: 75px;
    width: 783px;
    height: 20px;
    background: var(--band);
  }
  .band-presents { top: 210px; text-align: center; }
  .band-presents span {
    font-family: "Oswald", sans-serif;
    font-weight: 400;
    font-size: 15px;
    line-height: 20px;
    letter-spacing: 0.5px;
  }
  .band-mid { top: 646px; }
  .band-low { top: 850px; }
  .band-foot { top: 1178px; }
  .title-once {
    position: absolute;
    top: 230px;
    left: 0;
    width: 100%;
    text-align: center;
    font-family: "Montserrat", sans-serif;
    font-weight: 900;
    font-size: 272px;
    line-height: 1;
    letter-spacing: -8px;
  }
  .title-script {
    position: absolute;
    top: 462px;
    left: 0;
    width: 100%;
    text-align: center;
    font-family: "Yellowtail", "Satisfy", cursive;
    font-size: 140px;
    line-height: 1.1;
    padding-left: 40px;
    white-space: nowrap;
  }
  .workshop-label {
    position: absolute;
    top: 683px;
    left: 75px;
    font-family: "Oswald", sans-serif;
    font-weight: 600;
    font-size: 62px;
    line-height: 80px;
    text-transform: uppercase;
    letter-spacing: -0.5px;
    transform: scaleX(0.68);
    transform-origin: left top;
    white-space: nowrap;
  }
  .divider {
    position: absolute;
    left: 310px;
    top: 686px;
    width: 1px;
    height: 144px;
    background: var(--white);
    opacity: 0.7;
  }
  .blurb {
    position: absolute;
    top: 682px;
    left: 333px;
    width: 519px;
    font-family: "Roboto Condensed", sans-serif;
    font-size: 16px;
    line-height: 21.6px;
  }
  .blurb p + p { margin-top: 21.6px; }
  .blurb .line { display: block; white-space: nowrap; }
  .blurb .line-full { text-align: justify; text-align-last: justify; }
  .blurb strong { color: var(--yellow); font-weight: 700; }
  .date-month {
    position: absolute;
    top: 892px;
    left: 116px;
    font-family: "Archivo Black", sans-serif;
    font-size: 104px;
    line-height: 1;
    color: transparent;
    -webkit-text-stroke: 1.5px var(--white);
    letter-spacing: 4px;
    word-spacing: 18px;
    white-space: nowrap;
  }
  .date-days {
    position: absolute;
    top: 1000px;
    left: 114px;
    font-family: "Arimo", sans-serif;
    font-weight: 700;
    font-size: 80px;
    line-height: 1;
    letter-spacing: 1px;
    white-space: nowrap;
  }
  .slash {
    position: absolute;
    width: 1.5px;
    background: var(--white);
    transform: rotate(22deg);
  }
  .slash-time { left: 690px; top: 1020px; height: 56px; }
  .slash-price { left: 482px; top: 1098px; height: 54px; }
  .time {
    position: absolute;
    top: 1014px;
    left: 712px;
    font-family: "Arimo", sans-serif;
    font-size: 31px;
    line-height: 30px;
    letter-spacing: -1px;
  }
  .age {
    position: absolute;
    top: 1094px;
    left: 128px;
    font-family: "Roboto", sans-serif;
    font-weight: 300;
    font-size: 50px;
    line-height: 1;
    white-space: nowrap;
  }
  .price {
    position: absolute;
    top: 1092px;
    left: 502px;
    font-family: "Arimo", sans-serif;
    font-size: 33px;
    line-height: 30px;
    text-align: center;
    white-space: nowrap;
  }
</style>
</head>
<body>
<main class="flyer">
  <div class="scene" role="img" aria-label="Illustrated sunset over a calm sea with distant mountains, magenta sky fading into deep blue water"></div>

  <header class="academy">
    <div class="academy-name">moonbeam</div>
    <div class="academy-sub">Academy of Dance and Performing Arts</div>
  </header>

  <div class="band band-presents"><span>PRESENTS</span></div>

  <h1 class="title-once">ONCE</h1>
  <div class="title-script">Upon a Time</div>

  <div class="band band-mid"></div>

  <h2 class="workshop-label">Easter<br>Workshops</h2>
  <div class="divider"></div>
  <div class="blurb">
    <p>
      <span class="line line-full">This spring, your child will enjoy a joyous journey to the magical world</span>
      <span class="line">of Once Upon a Time for a fabulous springtime treat.</span>
    </p>
    <p>
      <span class="line line-full">We will work our magic to ensure your child enjoys every minute.</span>
      <span class="line line-full">Guiding each child every step of the way and inspire and encourage</span>
      <span class="line line-full">them to project their voices, learn energetic dance routines, sing catchy</span>
      <span class="line">songs, and more importantly <strong>HAVE FUN!</strong></span>
    </p>
  </div>

  <div class="band band-low"></div>

  <div class="date-month">April 2016</div>
  <div class="date-days">Tue 5 &amp; Wed 6</div>
  <div class="slash slash-time"></div>
  <div class="time">10AM<br>12PM</div>

  <div class="age">Age 3 – 7 years</div>
  <div class="slash slash-price"></div>
  <div class="price">$18 per day or<br>$30 for both days</div>

  <div class="band band-foot"></div>
</main>
</body>
</html>
```